Harrow Bend Family Law magazine ad

I need an ad that will run in Marlow Creek Living Magazine here in NC. The ad will be a 1/2 page ad, (7.25X4.875). Resolution is 300 dpi or higher.

We are a family law firm (divorce) and we want to high light child custody issues. I would like the ad copy to include our logo (which you can find on our website www.harrowbendfamilylaw.com) and I can send a high res one if you are chosen. Ad MUST include our address and phone number by state law.

Ad copy will be something about protecting children (something brief) like "Protect what you love" or something like that. I will pick quick as I have to turn it in on Wednesday. You will need to be able to email the final product to graphics@marlowcreeklivingmag.com and me too.

Target Market(s)

Married couples with kids (primarily men) ages 35-50

Industry/Entity Type

Legal

Colors
85cae6
cadf82
fbee3f
fbf289
33a6d7
33b8a4
add136

Requirements
Must have
• website, logo, address, and phone number
Nice to have
• creative and heart provoking (I want the image to make me want to act)
Should not have
• Don't be boring or give me some stock photo I have seen in a million divorce ads.

```html
<!DOCTYPE html>
<html lang="en">
<head>
<meta charset="utf-8">
<title>Harrow Bend Family Law – Half Page Ad</title>
<link href="https://fonts.googleapis.com/css2?family=Raleway:wght@300;400&display=swap" rel="stylesheet">
<style>
  :root {
    --sky: #29abe2;
    --white: #ffffff;
    --ink: #2b2b2b;
    --brand-blue: #33a6d7;
    --brand-green: #add136;
  }
  * { margin: 0; padding: 0; box-sizing: border-box; }
  html, body { width: 1200px; height: 807px; overflow: hidden; background: var(--white); }
  body { font-family: "Raleway", sans-serif; }
  .ad { position: relative; width: 1200px; height: 807px; }
  .hero { position: absolute; left: 0; top: 0; width: 1200px; height: 705px; background: var(--sky); color: var(--white); }
  .lead {
    position: absolute; right: calc(1200px - 374px); top: 248px;
    text-align: right; font-weight: 400; font-size: 24px; line-height: 28px; text-transform: uppercase;
    letter-spacing: 0.3px;
  }
  .divider { position: absolute; left: 388px; top: 234px; width: 2px; height: 110px; background: var(--white); }
  .headline {
    position: absolute; left: 398px; top: 214px;
    font-weight: 300; font-size: 146px; line-height: 150px; letter-spacing: -2px; white-space: nowrap;
  }
  .invite {
    position: absolute; right: calc(1200px - 947px); top: 356px; text-align: right; font-weight: 300;
  }
  .invite .note { font-size: 21px; line-height: 28px; }
  .invite .call { font-size: 27px; line-height: 36px; font-weight: 400; }
  .footer { position: absolute; left: 0; top: 705px; width: 1200px; height: 102px; background: var(--white); }
  .brand { position: absolute; left: 106px; top: 30px; display: flex; align-items: center; gap: 10px; }
  .brand-mark { width: 40px; height: 40px; border-radius: 50%; background: var(--brand-green); }
  .brand-name { font-size: 17px; font-weight: 400; color: var(--brand-blue); text-transform: uppercase; letter-spacing: 0.5px; }
  .contact {
    position: absolute; left: 761px; top: 19px; font-style: normal;
    font-size: 12px; line-height: 13.5px; color: var(--ink); font-weight: 400;
  }
</style>
</head>
<body>
<div class="ad">
  <section class="hero">
    <p class="lead">Your child<br>did not file<br>for&nbsp; divorce.</p>
    <span class="divider"></span>
    <h1 class="headline">YOU DID.</h1>
    <div class="invite">
      <p class="note">Discuss your child’s protection with us.</p>
      <p class="call">Call 910-555-0172</p>
    </div>
  </section>
  <footer class="footer">
    <div class="brand">
      <span class="brand-mark"></span>
      <span class="brand-name">Harrow Bend Family Law</span>
    </div>
    <address class="contact">
      1420 Alder Point Road, Suite 210, Harrow Bend, NC 28590<br>
      Email: ellen@harrowbendfamilylaw.com<br>
      Phone: 910-555-0172<br>
      Fax: 877-555-0193<br>
      Web: www.harrowbendfamilylaw.com
    </address>
  </footer>
</div>
</body>
</html>
```